Personal Injury Funding Flyer

We are Qorva Financial, a provider of receivables management solutions to the surgical industry.
We want a 1 page flyer to showcase our Motor Vehicle Accident (MVA) and Personal Injury (PI) case management and lien purchasing.

1- a flyer from a competitor. We like the overall feel of the flyer and the simplicity of the information presented.

You can also check out our website for examples of our company's style
www.qorvafinancial-example.com

Target Market(s)

Surgeons, office managers, administrators and CFOS at smaller surgical facilities and surgical hospitals nationwide

Industry/Entity Type

Financial

Requirements
Must have
• Titled: Personal Injury Case Funding
• Tagline: We Ensure Your Cases are Financially Sound
• Include Qorva Financial's logo
• Be sure to boldly highlight the 3 points:
• 3 Steps to Successful PI Case Management
• 1) Evaluate Cases
• Evaluate the financial aspects of the case including policy limits.
• 2) Consult Attorneys
• Evaluate the case background and likelihood of settlement.
• 3) Guaranteed Funding
• 15 day funding on most cases.
• How Does MVA/PI Funding Work?
• We pay you upfront and wait for the case to settle.
• Our funding eliminates the risk, hassle and uncertainty associated with PI cases.
• You get paid 100% NON-RECOURSE
• Include contact phone number (800) 472-5190
• >No Hassles
• >No Risk
• >Guaranteed Funds.
Nice to have
• Smiling doctor picture
Should not have
• Too much information

```html
<!DOCTYPE html>
<html lang="en">
<head>
<meta charset="utf-8">
<title>Qorva Financial – Personal Injury Case Funding</title>
<link href="https://fonts.googleapis.com/css2?family=Oswald:wght@500;600&family=Jost:wght@400;500;700&display=swap" rel="stylesheet">
<style>
  :root {
    --backdrop: #e9e9ea;
    --paper: #f4f4f4;
    --band-grey: #76767a;
    --maroon: #4a1414;
    --maroon-deep: #3d0f0f;
    --ink: #2b2b2b;
    --muted: #666666;
    --white: #ffffff;
    --bullet: #d8d8d8;
  }
  * { box-sizing: border-box; margin: 0; padding: 0; }
  html, body { width: 1089px; height: 1200px; overflow: hidden; }
  body { background: var(--backdrop); font-family: "Jost", sans-serif; color: var(--ink); }

  .flyer {
    position: absolute; left: 165px; top: 45px;
    width: 760px; height: 1110px;
    background: var(--paper);
    box-shadow: 0 12px 30px rgba(0,0,0,.28);
    overflow: hidden;
  }

  .title-band {
    height: 125px; background: var(--band-grey);
    display: flex; flex-direction: column; align-items: center; justify-content: center;
    color: var(--white); text-align: center;
  }
  .title-band h1 {
    font-family: "Oswald", sans-serif; font-weight: 600; font-size: 46px; line-height: 1.1;
  }
  .title-band .tagline-line {
    font-family: "Jost", sans-serif; font-weight: 500; font-size: 19px; margin-top: 4px;
  }

  .hero-photo {
    position: absolute; left: 30px; top: 125px; width: 730px; height: 435px;
    background: linear-gradient(125deg, #7e99b8 0%, #a9bccf 22%, #3c4b5c 40%, #dfe3e7 58%, #f1f1f1 78%, #c9ccd0 100%);
  }

  .intro {
    position: absolute; left: 50px; top: 578px; width: 355px;
    font-size: 16px; line-height: 1.25; text-align: justify;
  }
  .intro h2 {
    font-family: "Oswald", sans-serif; font-weight: 600; font-size: 21px;
    color: var(--maroon); text-align: left; margin-bottom: 8px;
  }
  .intro p + p { margin-top: 8px; }
  .intro strong { color: var(--maroon); }
  .promise {
    margin-top: 10px; list-style: none; display: flex; gap: 14px;
    font-weight: 700; font-size: 15px; color: var(--maroon);
  }

  .steps-heading {
    position: absolute; left: 420px; top: 585px; width: 320px;
    padding-left: 20px;
    font-family: "Oswald", sans-serif; font-weight: 600; font-size: 24px; line-height: 28px;
    color: var(--maroon); text-transform: uppercase;
  }
  .steps {
    position: absolute; left: 420px; top: 650px; width: 320px; height: 262px;
    background: var(--maroon); color: var(--white);
    list-style: none; padding: 20px 20px 0 22px;
  }
  .steps li { position: relative; padding-left: 32px; margin-bottom: 16px; }
  .steps li::before {
    content: ""; position: absolute; left: 0; top: 5px;
    width: 13px; height: 13px; border-radius: 50%; background: var(--bullet);
  }
  .steps .step-title { display: block; font-weight: 700; font-size: 18px; line-height: 1.2; }
  .steps .step-text { display: block; font-size: 15px; line-height: 1.25; margin-top: 3px; }

  .process-flow { position: absolute; left: 28px; top: 768px; width: 390px; height: 150px; }
  .process-flow text { font-family: "Jost", sans-serif; font-weight: 700; font-size: 7.5px; fill: var(--white); text-anchor: middle; }

  .brand-row {
    position: absolute; left: 50px; top: 932px; width: 690px;
    display: flex; align-items: center; gap: 18px;
  }
  .brand-mark { display: flex; align-items: center; gap: 10px; }
  .brand-square { width: 22px; height: 22px; background: var(--maroon); }
  .brand-name { font-size: 30px; font-weight: 500; color: var(--ink); line-height: 1; }
  .brand-tagline {
    border-left: 1px solid #999; padding-left: 10px;
    font-size: 14px; line-height: 1.15;
  }
  .brand-tagline span { display: block; }
  .brand-tagline span:first-child { color: var(--maroon); }
  .brand-tagline span:last-child { color: var(--muted); }

  .footer-band {
    position: absolute; left: 0; bottom: 0; width: 100%; height: 110px;
    background: var(--maroon-deep); color: var(--white);
    display: flex; flex-direction: column; align-items: center; justify-content: center;
  }
  .footer-band .site { font-weight: 700; font-size: 36px; line-height: 1.1; }
  .footer-band .phone { font-weight: 500; font-size: 22px; margin-top: 2px; }
</style>
</head>
<body>
<main class="flyer">
  <header class="title-band">
    <h1>Personal Injury Case Funding</h1>
    <p class="tagline-line">We Ensure Your Cases are Financially Sound</p>
  </header>

  <div class="hero-photo" role="img" aria-label="Photo of a stethoscope and pen resting on medical lab report papers and blue folders"></div>

  <section class="intro">
    <h2>How Does MVA/PI Funding Work?</h2>
    <p>We pay you upfront and wait for the case to settle.</p>
    <p>Our funding eliminates the risk, hassle and uncertainty associated with PI cases.</p>
    <p>You get paid <strong>100% NON-RECOURSE</strong>.</p>
    <ul class="promise">
      <li>&gt; No Hassles</li>
      <li>&gt; No Risk</li>
      <li>&gt; Guaranteed Funds</li>
    </ul>
  </section>

  <h2 class="steps-heading">3 Steps to Successful<br>PI Case Management</h2>
  <ol class="steps">
    <li><span class="step-title">1) Evaluate Cases</span><span class="step-text">Evaluate the financial aspects of the case including policy limits.</span></li>
    <li><span class="step-title">2) Consult Attorneys</span><span class="step-text">Evaluate the case background and likelihood of settlement.</span></li>
    <li><span class="step-title">3) Guaranteed Funding</span><span class="step-text">15 day funding on most cases.</span></li>
  </ol>

  <svg class="process-flow" viewBox="0 0 390 150" aria-label="Case funding process">
    <g fill="#8a8a8e">
      <path d="M30 38 A40 40 0 0 1 78 22 l2 -8 10 16 -16 6 2 -6 A32 32 0 0 0 36 44z"/>
      <path d="M110 38 A40 40 0 0 1 158 22 l2 -8 10 16 -16 6 2 -6 A32 32 0 0 0 116 44z"/>
      <path d="M190 38 A40 40 0 0 1 238 22 l2 -8 10 16 -16 6 2 -6 A32 32 0 0 0 196 44z"/>
      <path d="M80 112 A40 40 0 0 0 118 118 l0 8 14 -14 -16 -6 0 6 A32 32 0 0 1 86 104z"/>
      <path d="M160 112 A40 40 0 0 0 198 118 l0 8 14 -14 -16 -6 0 6 A32 32 0 0 1 166 104z"/>
      <path d="M278 60 l24 -6 0 -6 12 12 -12 12 0 -6 -24 6z"/>
      <path d="M278 80 l24 12 2 -6 8 14 -16 4 2 -6 -24 -12z"/>
      <circle cx="40" cy="70" r="32"/>
      <circle cx="120" cy="75" r="32"/>
      <circle cx="200" cy="70" r="32"/>
      <circle cx="260" cy="75" r="30"/>
    </g>
    <circle cx="346" cy="45" r="30" fill="#4a1414"/>
    <circle cx="338" cy="112" r="30" fill="#4a1414"/>
    <text x="40" y="62"><tspan x="40">Patient referred</tspan><tspan x="40" dy="9">by physician</tspan><tspan x="40" dy="9">or attorney</tspan></text>
    <text x="120" y="67"><tspan x="120">Facility submits</tspan><tspan x="120" dy="9">request form</tspan><tspan x="120" dy="9">for screening</tspan></text>
    <text x="200" y="62"><tspan x="200">Team screens</tspan><tspan x="200" dy="9">policy limits</tspan><tspan x="200" dy="9">and liability</tspan></text>
    <text x="260" y="67"><tspan x="260">Approved cases</tspan><tspan x="260" dy="9">are funded</tspan><tspan x="260" dy="9">and billed</tspan></text>
    <text x="346" y="37"><tspan x="346">Approved</tspan><tspan x="346" dy="9">cases paid</tspan><tspan x="346" dy="9">within 15 days</tspan></text>
    <text x="338" y="104"><tspan x="338">Denied cases</tspan><tspan x="338" dy="9">sent back</tspan><tspan x="338" dy="9">for follow up</tspan></text>
  </svg>

  <div class="brand-row">
    <div class="brand-mark">
      <span class="brand-square"></span>
      <span class="brand-name">Qorva Financial</span>
    </div>
    <div class="brand-tagline"><span>Receivable</span><span>Management</span><span>Solutions</span></div>
  </div>

  <footer class="footer-band">
    <span class="site">www.qorvafinancial-example.com</span>
    <span class="phone">(800) 472-5190</span>
  </footer>
</main>
</body>
</html>
```